" Atendimento em clínica especializada de otorrino na região do Ipiranga (São Paulo - SP), prestando atendimento médico, realizando exames e cirurgias na área. "

```html
<!DOCTYPE html>
<html lang="pt-BR">
<head>
<meta charset="UTF-8">
<title>Dr. Henrique Moraes – Cartão de visita</title>
<link rel="stylesheet" href="https://fonts.googleapis.com/css2?family=Montserrat:wght@500;600;700&family=Open+Sans:wght@400;600&display=swap">
<style>
  :root {
    --navy: #0f2b40;
    --navy-deep: #0b2233;
    --blue: #1b8fc7;
    --blue-light: #3aa9dc;
    --paper: #ffffff;
    --ink: #4a5560;
    --rule: #c9d2d9;
    --stage: #eef0f2;
  }
  * { margin: 0; padding: 0; box-sizing: border-box; }
  html, body { width: 1200px; height: 1200px; overflow: hidden; }
  body {
    background: var(--stage);
    font-family: "Open Sans", sans-serif;
    position: relative;
  }
  .card {
    position: absolute;
    left: 150px;
    width: 900px;
    height: 500px;
    border-radius: 28px;
    overflow: hidden;
    box-shadow: 0 10px 30px rgba(0,0,0,0.12);
  }
  .card--front { top: 70px; background: var(--paper); }
  .card--back { top: 630px; background: var(--navy); }

  /* front */
  .contact {
    position: absolute;
    left: 56px;
    top: 60px;
    width: 360px;
  }
  .contact__name {
    font-family: "Montserrat", sans-serif;
    font-weight: 600;
    font-size: 30px;
    color: var(--blue);
    line-height: 1.1;
  }
  .contact__reg {
    font-size: 17px;
    color: var(--ink);
    margin-top: 4px;
    margin-bottom: 30px;
  }
  .contact__list { list-style: none; }
  .contact__item {
    display: flex;
    align-items: flex-start;
    gap: 14px;
    font-size: 17px;
    color: var(--ink);
    line-height: 1.25;
    margin-bottom: 16px;
  }
  .contact__icon {
    flex: 0 0 28px;
    width: 28px;
    height: 28px;
    border-radius: 50%;
    background: var(--blue);
    display: flex;
    align-items: center;
    justify-content: center;
  }
  .contact__icon svg { width: 15px; height: 15px; fill: #fff; }
  .divider {
    position: absolute;
    left: 450px;
    top: 40px;
    width: 1px;
    height: 330px;
    background: var(--rule);
  }
  .brand {
    position: absolute;
    left: 470px;
    top: 150px;
    width: 410px;
    text-align: center;
  }
  .brand__mark {
    width: 70px;
    height: 70px;
    border-radius: 50%;
    background: var(--blue);
    margin: 0 auto 18px;
  }
  .brand__name {
    font-family: "Montserrat", sans-serif;
    font-weight: 700;
    font-size: 33px;
    color: var(--navy);
    letter-spacing: 0.5px;
  }
  .brand__field {
    font-family: "Montserrat", sans-serif;
    font-weight: 500;
    font-size: 15px;
    color: var(--blue);
    letter-spacing: 5px;
    margin-top: 6px;
  }
  .band { position: absolute; left: 0; bottom: 0; width: 900px; height: 80px; }

  /* back */
  .brand--back { left: 0; width: 900px; top: 120px; }
  .brand--back .brand__mark { width: 90px; height: 90px; margin-bottom: 26px; }
  .brand--back .brand__name { color: #fff; font-size: 42px; }
  .brand--back .brand__field { font-size: 17px; letter-spacing: 7px; margin-top: 8px; }
</style>
</head>
<body>

<section class="card card--front">
  <div class="contact">
    <h1 class="contact__name">Dr. Henrique Moraes</h1>
    <p class="contact__reg">CRM UF-000000</p>
    <ul class="contact__list">
      <li class="contact__item">
        <span class="contact__icon"><svg viewBox="0 0 24 24"><path d="M6.6 10.8a15.1 15.1 0 0 0 6.6 6.6l2.2-2.2c.3-.3.7-.4 1-.2 1.1.4 2.3.6 3.6.6.6 0 1 .4 1 1V20c0 .6-.4 1-1 1A17 17 0 0 1 3 4c0-.6.4-1 1-1h3.5c.6 0 1 .4 1 1 0 1.3.2 2.5.6 3.6.1.3 0 .7-.2 1z"/></svg></span>
        <span>(00) 0000-0000</span>
      </li>
      <li class="contact__item">
        <span class="contact__icon"><svg viewBox="0 0 24 24"><path d="M3 5h18v14H3z M3 5l9 7 9-7" fill="none" stroke="#fff" stroke-width="2"/></svg></span>
        <span>contato@exemplo.com.br</span>
      </li>
      <li class="contact__item">
        <span class="contact__icon"></span>
        <span>www.exemplo.com.br</span>
      </li>
      <li class="contact__item">
        <span class="contact__icon"><svg viewBox="0 0 24 24"><path d="M12 2a7 7 0 0 0-7 7c0 5.2 7 13 7 13s7-7.8 7-13a7 7 0 0 0-7-7zm0 9.5A2.5 2.5 0 1 1 12 6.5a2.5 2.5 0 0 1 0 5z"/></svg></span>
        <span>rua exemplo, sl 000<br>cidade-UF, CEP: 00000-000</span>
      </li>
    </ul>
  </div>
  <div class="divider"></div>
  <div class="brand">
    <div class="brand__mark"></div>
    <p class="brand__name">DR. HENRIQUE MORAES</p>
    <p class="brand__field">OTORRINOLARINGOLOGIA</p>
  </div>
  <svg class="band" viewBox="0 0 900 80" preserveAspectRatio="none" aria-hidden="true">
    <path d="M0 70 L300 70 C340 70 350 40 390 40 L900 40 L900 80 L0 80 Z" fill="var(--blue)"/>
    <path d="M0 74 L300 74 C340 74 350 50 392 50 L900 50 L900 80 L0 80 Z" fill="var(--blue-light)" opacity="0.6"/>
  </svg>
</section>

<section class="card card--back">
  <div class="brand brand--back">
    <div class="brand__mark"></div>
    <p class="brand__name">DR. HENRIQUE MORAES</p>
    <p class="brand__field">OTORRINOLARINGOLOGIA</p>
  </div>
  <svg class="band" viewBox="0 0 900 80" preserveAspectRatio="none" aria-hidden="true">
    <path d="M260 80 C290 80 300 62 330 62 L660 62 C690 62 700 80 730 80 Z" fill="var(--blue)"/>
  </svg>
</section>

</body>
</html>
```